Label Design for 2x Chutney Products

We need a label design for 2x Chutney Products.
Mellora Chutney - Red Chili
Mellora Chutney - Green Chili & Coriander
See attached pictures. This is just sample pictures so you get an impression of the product and the colors. Both labels to have as title the generic name "Mellora Chutney" and then added either Red Chili or Green Chili & Coriander. The different terms needs to be good readable and can differ in font/color/size, or in the same style if this makes more sense from design point (as I am not a designer). The labels later on need to be editable in the way that the ingredient list, nutrition list, basis company and production information can be added. If this needs to be done directly and cannot be edited later on please let know. Editable design related the additional text also would be good as the additional information need to be added in different languages (Dutch. German and perhaps French). No clue how this is to be implemented but looking forward to receive some input/solutions on this.
I already had a project to create the company logo. I consider this logo to be used as the product logo and not the company logo. A different company logo later on can be designed from new. This logo is here attached. Either to work with this logo and use it as product logo (perhaps revise the colors) and add the product description or create a new logo for the product from scratch if you feel too. The logo itself should be easily readable for the product name/description and the colors appealing to such product and of course customers.
Please contact if any clarification needed. Thanks in advance for your efforts and ideas for this project.

Industry/Entity Type

Food

Other font styles liked:
• Asian Touch

Requirements
Nice to have
• If possible "simply" editable for text fields in order to add/revise the ingredient list, nutrition list, revise to different languages.

```html
<!DOCTYPE html>
<html lang="en">
<head>
<meta charset="utf-8">
<title>Mellora Chutney – Red Chili Label</title>
<link rel="stylesheet" href="https://fonts.googleapis.com/css2?family=Amatic+SC:wght@700&family=Montserrat:wght@700&family=Roboto:wght@400&display=swap">
<style>
  :root {
    --page-bg: #e9e9ea;
    --label-red-dark: #bd121d;
    --label-red-light: #ec605d;
    --chili-red: #cf1a20;
    --chili-deep: #a30e16;
    --badge-white: #ffffff;
    --ink: #1c1c1c;
    --accent-red: #d7252b;
    --brand-dot: #d9342b;
    --body-white: #ffffff;
  }
  html, body {
    margin: 0;
    padding: 0;
    width: 946px;
    height: 1200px;
    overflow: hidden;
    background: var(--page-bg);
  }
  .label {
    position: absolute;
    left: 0;
    top: 473px;
    width: 946px;
    height: 254px;
    overflow: hidden;
  }
  .label svg { display: block; }
  .ingredients {
    font-family: "Roboto", Arial, sans-serif;
    font-size: 8.3px;
    fill: var(--body-white);
  }
  .brand-name {
    font-family: "Montserrat", Arial, sans-serif;
    font-weight: 700;
    font-size: 11.5px;
    fill: var(--ink);
    letter-spacing: 0.2px;
  }
  .product-title {
    font-family: "Amatic SC", cursive;
    font-weight: 700;
    font-size: 50px;
    fill: var(--ink);
  }
  .product-variant {
    font-family: "Amatic SC", cursive;
    font-weight: 700;
    font-size: 34px;
    fill: var(--accent-red);
  }
</style>
</head>
<body>
  <section class="label">
    <svg width="946" height="254" viewBox="0 0 946 254">
      <defs>
        <linearGradient id="label-band" x1="0" y1="0" x2="1" y2="0">
          <stop offset="0" stop-color="var(--label-red-dark)"/>
          <stop offset="1" stop-color="var(--label-red-light)"/>
        </linearGradient>
        <radialGradient id="chili-field" cx="0.5" cy="0.55" r="0.6">
          <stop offset="0" stop-color="var(--chili-red)"/>
          <stop offset="1" stop-color="var(--chili-deep)"/>
        </radialGradient>
      </defs>

      <rect class="label-band" x="0" y="0" width="946" height="254" fill="url(#label-band)"/>

      <rect class="chili-photo" x="250" y="0" width="453" height="254" fill="url(#chili-field)" role="img" aria-label="Photograph of fresh red chili peppers arranged around the badge"/>

      <text class="ingredients">
        <tspan x="37" y="55">Ingredients: Lorem ipsum dolor sit amet,</tspan>
        <tspan x="37" y="65.3">consectetur adipiscing elit, sed do eiusmod</tspan>
        <tspan x="37" y="75.6">tempor incididunt ut labore et dolore magna</tspan>
        <tspan x="37" y="85.9">aliqua. Et sollicitudin ac orci phasellus</tspan>
        <tspan x="37" y="96.2">egestas.</tspan>
      </text>

      <circle class="badge" cx="472" cy="137" r="133" fill="var(--badge-white)"/>

      <g class="brand">
        <circle class="brand-dot" cx="472" cy="66" r="21" fill="var(--brand-dot)"/>
        <text class="brand-name" x="472" y="104" text-anchor="middle">TAVELO</text>
        <text class="brand-name" x="472" y="116" text-anchor="middle">FOODS</text>
      </g>

      <text class="product-title" x="472" y="170" text-anchor="middle" textLength="218" lengthAdjust="spacingAndGlyphs">Mellora Chutney</text>
      <text class="product-variant" x="472" y="217" text-anchor="middle" textLength="78" lengthAdjust="spacingAndGlyphs">Red Chili</text>
    </svg>
  </section>
</body>
</html>
```